Book Cover Design Project

Need a hip, slightly edgy (even a little bit sexy) cover design for a book about The Millennial Generation.

"Pathfinders 202" is a non-fiction book. The target audience/customer is the younger Baby Boomer and most of Generation X, looking to better understand the largest generation on the planet (Millennials). So, the cover should tease the young, hip, edgy vibe of Millennials...without looking too alienating to someone in their 40's or 50's.

Imagine this as a movie poster for a documentary about Millennials-you want to have a cover that intrigues the audience and reminds them that the topic is something the audience doesn't completely understand, without making them feel like it's too cool.

Much of the target audience was the initial audience for QRX, when it started in the early 80's. They're cooler than you might think, and like to think of themselves that way.

Possible inspiration:

-Retro Peter Calloway movie posters (with an irreverent, contemporary nod to the original)
-Iconic Magazine covers from the 80's or 90's (Think Velvet Lantern)
-Stark, fresh, contemporary imagery/style that feels very Brooklyn/Austin/Silverlake in it's vibe.

The final design should convey that this book is a great resource to crack the code of who millennials are, why they are so different, and how to live with that reality.
Updates

Project Deadline Extended
Reason: Seeing some great work. Been traveling, so can't make a decision right now.

Industry/Entity Type

Movie

Requirements
Must have
• The Title:
"Pathfinders 202"

Subtitle:
"Understanding and Engaging the largest generation on the planet"

(open to most fonts, etc)
Nice to have
• A crisp, recognizable cover that feels like a movie poster or a magazine.
Should not have
• Predictable, cheesy stock photography.

```html
<!DOCTYPE html>
<html lang="en">
<head>
<meta charset="utf-8">
<title>Pathfinders 202 — Book Cover</title>
<link rel="stylesheet" href="https://fonts.googleapis.com/css2?family=Inter:wght@700;800&display=swap">
<style>
  :root {
    --room-dark: #1c1510;
    --room-mid: #4a3524;
    --lamp-glow: #fff6e6;
    --warm-light: #b88a57;
    --type-white: #ffffff;
  }
  html, body {
    margin: 0;
    padding: 0;
    width: 800px;
    height: 1200px;
    overflow: hidden;
    background: var(--room-dark);
  }
  .cover {
    position: relative;
    width: 800px;
    height: 1200px;
    overflow: hidden;
    font-family: "Inter", "Helvetica Neue", Arial, sans-serif;
  }
  .cover-photo {
    position: absolute;
    inset: 0;
    background:
      radial-gradient(circle at 623px 365px, var(--lamp-glow) 0, rgba(255,240,215,0.85) 28px, rgba(210,160,100,0.35) 120px, rgba(0,0,0,0) 320px),
      radial-gradient(ellipse at 420px 760px, rgba(184,138,87,0.55) 0, rgba(120,85,55,0.3) 260px, rgba(0,0,0,0) 520px),
      linear-gradient(180deg, #2a2019 0%, var(--room-mid) 55%, #2b1e14 100%);
  }
  .title-line {
    position: absolute;
    left: -8px;
    margin: 0;
    font-size: 290px;
    font-weight: 800;
    line-height: 1;
    letter-spacing: -6px;
    color: var(--type-white);
    white-space: nowrap;
  }
  .title-line--1 { top: -12px; }
  .title-line--2 { top: 275px; }
  .title-line--3 { top: 562px; }
  .title-line--4 { top: 854px; }
  .subtitle {
    position: absolute;
    left: 0;
    top: 1156px;
    margin: 0;
    font-size: 14px;
    font-weight: 700;
    letter-spacing: 1.6px;
    text-transform: uppercase;
    color: var(--type-white);
    white-space: nowrap;
  }
</style>
</head>
<body>
  <main class="cover">
    <div class="cover-photo" role="img" aria-label="Dim warm-lit living room: a young woman on a brown sofa absorbed in her phone, laptop beside her, lit by a bright floor lamp"></div>
    <h1 class="book-title" aria-label="Pathfinders 202">
      <span class="title-line title-line--1">PATH</span>
      <span class="title-line title-line--2">FIN</span>
      <span class="title-line title-line--3">DERS</span>
      <span class="title-line title-line--4">202</span>
    </h1>
    <p class="subtitle">Understanding and engaging the largest generation on the planet</p>
  </main>
</body>
</html>
```